How likely are people to engage in social distancing? We need a good illustration to show the data!

We surveyed U.S. adults March 20th - 24th, 2020 and asked how likely they were to engage in social distancing (and other COVID-19 related health behaviors). What did the survey find? Basically, most people intend to engage in social distancing behaviors (e.g., avoiding large crowds) and other behaviors that reduce the spread of COVID-19 (e.g., washing hands at least 20 seconds). When most people intend to engage in a behavior, then public health professionals try to leverage that to move more people to act.
Now we need innovative and professional images that attempt to communicate one or all of these findings. The specific findings are nicely summarized in the attached document. For example, 82% of participants intend to engage in social distancing.
What sort of visual are we looking for? Our preference is for an original illustration (or set of illustrations). Our preference is for (creative and powerful illustrations, but we are also open to the creative and well-executed infographics.
We need these images fast . We will award monetary prizes to the 3 best designs. If we like more than that, then we might purchase more (e.g., in past contests, we have purchased as many as 30 designs).
What we will need:
(1) The illustrations must be original and we will need the photoshop and/or illustrator files for all artwork.
(2) You can illustrate all of the findings or just one of them. We need creative approaches that do a lucid job of bringing the data to life. Most people intend to engage in these behaviors. How to communicate that? Corvantists and Halmerites do not differ in their intentions; how to communicate that?
(3) The illustration should say, somewhere: "Based on a survey of 400 U.S. adults conducted March 20 - 24th, 2020."

U.S. Adults

• Original illustrations based on the findings of the survey (see attached document).

```html
<!DOCTYPE html>
<html lang="en">
<head>
<meta charset="UTF-8">
<title>Avoid touching your eyes, nose and mouth – 81%</title>
<link rel="stylesheet" href="https://fonts.googleapis.com/css2?family=Kaushan+Script&family=Marck+Script&display=swap">
<style>
  :root {
    --page-bg: #ffffff;
    --blob-sand: #e1d7c1;
    --stat-teal: #1ba8bb;
    --ink-plum: #2f2a44;
    --hair-dark: #34304a;
    --skin-tan: #c4a77a;
    --sweater-peach: #f2c7ac;
  }
  html, body {
    margin: 0;
    padding: 0;
    overflow: hidden;
    background: var(--page-bg);
  }
  .canvas {
    position: relative;
    width: 1200px;
    height: 1200px;
    overflow: hidden;
    background: var(--page-bg);
  }
  .backdrop {
    position: absolute;
    inset: 0;
  }
  .blob { fill: var(--blob-sand); }
  .illustration-slot {
    position: absolute;
    left: 570px;
    top: 365px;
    width: 360px;
    height: 505px;
    border-radius: 170px 170px 120px 120px;
    background: linear-gradient(180deg, var(--hair-dark) 0%, var(--skin-tan) 45%, var(--sweater-peach) 75%);
  }
  .stat-value {
    position: absolute;
    left: 330px;
    top: 372px;
    margin: 0;
    font-family: "Kaushan Script", cursive;
    font-size: 140px;
    line-height: 1;
    font-weight: 400;
    color: var(--stat-teal);
    letter-spacing: -2px;
  }
  .stat-caption {
    position: absolute;
    left: 230px;
    top: 555px;
    margin: 0;
    font-family: "Marck Script", cursive;
    font-size: 56px;
    line-height: 84px;
    color: var(--ink-plum);
    white-space: nowrap;
  }
</style>
</head>
<body>
  <main class="canvas">
    <svg class="backdrop" width="1200" height="1200" viewBox="0 0 1200 1200" aria-hidden="true">
      <path class="blob" d="M 560 238 C 650 230, 720 280, 790 280 C 870 280, 950 340, 975 420 C 1000 500, 1010 620, 1010 700 C 1010 860, 880 940, 700 970 C 520 1000, 330 960, 250 880 C 180 810, 180 720, 195 600 C 210 480, 230 380, 330 300 C 390 255, 470 242, 560 238 Z"/>
    </svg>
    <div class="illustration-slot" role="img" aria-label="Illustration of a woman with dark curly hair and a peach sweater, shown from the shoulders up, holding her hands to her face"></div>
    <p class="stat-value">81%</p>
    <p class="stat-caption">Avoid touching your<br>eyes, nose and mouth</p>
  </main>
</body>
</html>
```